R4 Pips (CBD candy infused with Delta-8)

The proposed logo are two pool table balls. One is a D and the other is an 8, its a brand and we need a label for Gummy human treats. This treats are being infused with Delt-8. I i will upload examples only. The example is of the type of labels needed (package and label for bottle)

Target Market(s)

Your professionals

Font styles to use
Sans Serif

Requirements
Must have
• Youthful look
Nice to have
• Consider using the Delta symbol instead of the D.
Also, I provided a sample of a label that's used on two type of packages.

```html
<!DOCTYPE html>
<html lang="en">
<head>
<meta charset="utf-8">
<title>R4 Pips – Sleep Blend Gummies Label</title>
<link rel="stylesheet" href="https://fonts.googleapis.com/css2?family=Roboto:wght@400;700;900&display=swap">
<style>
  :root {
    --page: #ffffff;
    --label-top: #a8326f;
    --label-mid: #7e5a93;
    --label-bottom: #3d95b0;
    --panel-teal: #1f98bf;
    --panel-line: #1d2a33;
    --ink: #1a1a1a;
    --silver: #c9cad0;
    --magenta: #a3215f;
    --white: #ffffff;
  }
  * { box-sizing: border-box; margin: 0; padding: 0; }
  html, body {
    width: 1200px; height: 1200px; overflow: hidden;
    background: var(--page);
    font-family: "Roboto", Arial, sans-serif;
  }
  .label {
    position: absolute; left: 220px; top: 75px;
    width: 760px; height: 1050px;
    overflow: hidden;
  }
  .label__pattern {
    position: absolute; inset: 0;
    background: linear-gradient(180deg, var(--label-top) 0%, var(--label-mid) 45%, var(--label-bottom) 100%);
  }
  .title-panel {
    position: absolute; left: 75px; top: 0;
    width: 510px; height: 310px;
    background: var(--panel-teal);
  }
  .title-panel__frame {
    position: absolute; left: 42px; top: 38px; right: 12px; bottom: 38px;
    border: 2px solid var(--panel-line);
    display: flex; flex-direction: column; align-items: center; justify-content: center;
  }
  .title-panel__kicker {
    font-weight: 700; font-size: 30px; color: var(--ink); white-space: nowrap;
  }
  .title-panel__headline {
    font-weight: 900; font-size: 108px; line-height: 1.02;
    color: var(--silver);
  }
  .title-panel__sub {
    font-weight: 400; font-size: 34px; color: var(--ink); white-space: nowrap;
  }
  .brand {
    position: absolute; left: 0; top: 380px;
    width: 760px; height: 420px;
    display: flex; align-items: center; justify-content: center; gap: 36px;
  }
  .brand__dot {
    width: 200px; height: 200px; border-radius: 50%;
    background: var(--silver); flex: none;
  }
  .brand__name {
    font-weight: 900; font-size: 112px; color: var(--ink); white-space: nowrap;
  }
  .info-strip {
    position: absolute; left: 82px; right: 0; top: 836px;
    height: 214px;
    background: var(--magenta);
  }
  .info-strip__box {
    position: absolute; left: 30px; top: 38px; width: 218px; height: 128px;
    color: var(--white);
  }
  .info-strip__blend {
    font-weight: 700; font-size: 25px; white-space: nowrap;
    border-bottom: 2px solid rgba(255,255,255,0.8); padding-bottom: 2px;
  }
  .info-strip__count { font-size: 17px; margin-top: 12px; }
  .info-strip__weight { font-size: 17px; margin-top: 22px; white-space: nowrap; }
  .info-strip__dose {
    position: absolute; left: 300px; top: 58px; text-align: center; color: var(--white);
  }
  .info-strip__mg { font-weight: 700; font-size: 32px; line-height: 1; }
  .info-strip__unit { font-size: 16px; margin-top: 6px; white-space: nowrap; }
</style>
</head>
<body>
  <main class="label">
    <div class="label__pattern" role="img" aria-label="Fine zigzag stripe pattern shading from magenta to blue"></div>

    <section class="title-panel">
      <div class="title-panel__frame">
        <p class="title-panel__kicker">PREMIUM CBD EDIBLES</p>
        <h1 class="title-panel__headline">CBD</h1>
        <p class="title-panel__sub">Candy Infused Gummies</p>
      </div>
    </section>

    <section class="brand">
      <span class="brand__dot"></span>
      <span class="brand__name">R4 Pips</span>
    </section>

    <section class="info-strip">
      <div class="info-strip__box">
        <p class="info-strip__blend">SLEEP BLEND</p>
        <p class="info-strip__count">100 COUNT</p>
        <p class="info-strip__weight">Net Wt: 250g (8.8oz)</p>
      </div>
      <div class="info-strip__dose">
        <p class="info-strip__mg">1500MG</p>
        <p class="info-strip__unit">CBD PER BOTTLE</p>
      </div>
    </section>
  </main>
</body>
</html>
```